quendix.com redesign

We are a successful web hosting company that has been around since 1999 with 10,000 customers managing 2,000 websites and 12,000 domain names. Our challenge - we are losing ground because our site is getting old, our pricing is not competitive and our feature set needs to change to match the new world of mobile centric everything. We want to reach out to all of the domain names that we don't host websites for. We believe that if we designed a new site that focuses on bringing home all of those externally hosted websites to our own web hosting company that we would have a solid future. We need to compete against zelmorix.com, pellwarden.com, grumlane.com, birvon.com, olvestra.com, trekmoss.com, vandrift.com, nulvo.com and 100,000 others. We need to simplify our message with clean design, focused pages, easy decision making processes for the consumer. We use WHMCS for the background provisioning and billing so we can pretty much manage any kind of pricing model and discounted promotion packages.
I would prefer Twitter bootstrap CSS based responsive design.

Reason: I was away on vacation for 2 weeks - I just got back - I need time to fairly review all submissions - thank you for your patience. Tobin Farrow Quendix.com

Thanks to all who submitted sample designs - unfortunately most of them were nothing much more than already available templates with some of my current content and logo added to them. I will try to be more specific to reduce the number of choices. I need the template be fully compatible with WHMCS and Wordpress if you can't make it work with WHMCS directly. Another question I have to ask is -"exactly what am I getting for my $500.00 - is it just a PSD template or actual integration of that theme into WHMCS or Wordpress?"  I don't expect anyone to create new content for the site at that price. What do you charge if  you are able to create content or get directly involved in the site implementation of that template?

```html
<!DOCTYPE html>
<html lang="en">
<head>
<meta charset="utf-8">
<title>Quendix — Business Hosting</title>
<link href="https://fonts.googleapis.com/css2?family=Open+Sans:wght@400;600;700&display=swap" rel="stylesheet">
<style>
  :root {
    --sky: #4fbde9;
    --sky-deep: #2aa3d6;
    --white: #ffffff;
    --ink: #555a60;
    --muted: #9aa0a6;
    --line: #e3e6e9;
    --panel: #f1f2f4;
    --tier-head: #e4e6e8;
    --go: #2fc83c;
    --badge: #c4c8cc;
    --photo-a: #c9d7e2;
    --photo-b: #7d8fa0;
  }
  * { box-sizing: border-box; margin: 0; padding: 0; }
  html, body { width: 1200px; height: 827px; overflow: hidden; }
  body { font-family: "Open Sans", Arial, sans-serif; background: var(--white); color: var(--ink); position: relative; }

  .hero { position: absolute; left: 0; top: 0; width: 1200px; height: 470px; background: var(--sky); color: var(--white); overflow: hidden; }
  .site-header { position: absolute; left: 160px; right: 160px; top: 26px; height: 50px; display: flex; align-items: center; justify-content: space-between; }
  .brand { font-size: 40px; font-weight: 700; letter-spacing: -1px; color: var(--white); }
  .main-nav { display: flex; align-items: center; gap: 30px; font-size: 14px; }
  .main-nav .account { border: 1px solid var(--white); border-radius: 3px; padding: 4px 12px; }

  .domain-search { position: absolute; left: 170px; top: 120px; width: 860px; height: 56px; display: flex; background: var(--white); border-radius: 3px; overflow: hidden; }
  .domain-search .field { flex: 1; display: flex; align-items: center; padding: 0 18px; font-size: 14px; color: #a6abb0; }
  .domain-search .field b { color: #7d8288; font-weight: 600; margin: 0 4px; }
  .domain-search .field i { margin-left: 4px; }
  .domain-search .submit { width: 120px; background: var(--go); color: var(--white); font-weight: 700; font-size: 16px; display: flex; align-items: center; justify-content: center; }

  .hero-copy { position: absolute; left: 300px; top: 242px; width: 430px; }
  .hero-copy h1 { font-size: 27px; font-weight: 700; margin-bottom: 16px; }
  .hero-copy p { font-size: 15px; line-height: 1.6; margin-bottom: 20px; }
  .hero-copy .learn { display: inline-block; border: 1px solid var(--white); border-radius: 2px; padding: 4px 16px; font-size: 15px; }

  .hero-photo { position: absolute; left: 770px; top: 210px; width: 230px; height: 260px; background: linear-gradient(180deg, var(--photo-a), var(--photo-b)); border-radius: 110px 110px 0 0; }
  .slide-arrow { position: absolute; top: 300px; }
  .slide-arrow.prev { left: 80px; }
  .slide-arrow.next { right: 80px; }

  .awards { position: absolute; left: 0; top: 470px; width: 1200px; height: 74px; border-bottom: 1px solid var(--line); display: flex; align-items: center; justify-content: center; gap: 26px; }
  .awards .label { font-size: 13px; color: var(--muted); margin-right: 8px; }
  .awards .badge { width: 46px; height: 46px; border-radius: 50%; background: var(--badge); border: 3px solid #e2e4e6; }
  .awards .badge.wide { width: 70px; border-radius: 24px; }

  .packages { position: absolute; left: 0; top: 545px; width: 1200px; height: 282px; background: var(--white); }
  .packages h2 { text-align: center; font-size: 20px; font-weight: 400; color: var(--ink); margin-top: 16px; }
  .tiers { display: flex; justify-content: center; gap: 18px; margin-top: 16px; }
  .tier { width: 210px; background: var(--panel); }
  .tier-name { height: 30px; background: var(--tier-head); color: var(--muted); font-size: 13px; display: flex; align-items: center; justify-content: center; gap: 8px; }
  .tier-name::before { content: ""; width: 6px; height: 6px; border-radius: 50%; background: currentColor; }
  .tier.featured .tier-name { background: var(--sky-deep); color: var(--white); }
  .features { list-style: none; background: var(--white); border: 1px solid var(--line); padding: 6px 14px; }
  .features li { font-size: 11px; color: var(--muted); height: 19px; display: flex; align-items: center; gap: 8px; }
  .tier.featured .features li { color: var(--sky-deep); }
  .price { height: 72px; display: flex; flex-direction: column; align-items: center; justify-content: center; gap: 6px; }
  .price .amount { font-size: 24px; color: #a8adb2; font-weight: 600; }
  .price .amount small { font-size: 11px; font-weight: 400; }
  .tier.featured .price .amount { color: var(--sky-deep); }
  .price .order { font-size: 10px; background: #c8ccd0; color: var(--white); padding: 3px 12px; border-radius: 2px; }
  .tier.featured .price .order { background: var(--sky-deep); }
</style>
</head>
<body>
  <section class="hero">
    <header class="site-header">
      <div class="brand">quendix</div>
      <nav class="main-nav">
        <span>All Products</span>
        <span>Domain</span>
        <span>Website</span>
        <span>S.E.O. Toolkit</span>
        <span>Support</span>
        <span class="account">Login / Register</span>
      </nav>
    </header>

    <div class="domain-search">
      <div class="field">Enter a <b>domain name</b> here, Example: <i>www.yourdomain.com</i></div>
      <div class="submit">Search</div>
    </div>

    <div class="hero-copy">
      <h1>Our business is built to serve yours.</h1>
      <p>With a dedicated support team, industry-leading uptime that suit your business, it's no wonder Quendix is an award-winner leader in business hosting</p>
      <span class="learn">Learn More</span>
    </div>

    <div class="hero-photo" role="img" aria-label="Photo of a smiling support agent in business attire"></div>

    <svg class="slide-arrow prev" width="14" height="24" viewBox="0 0 14 24"><path d="M12 2 L2 12 L12 22" fill="none" stroke="#ffffff" stroke-width="2"/></svg>
    <svg class="slide-arrow next" width="14" height="24" viewBox="0 0 14 24"><path d="M2 2 L12 12 L2 22" fill="none" stroke="#ffffff" stroke-width="2"/></svg>
  </section>

  <section class="awards">
    <span class="label">Award on:</span>
    <span class="badge"></span>
    <span class="badge wide"></span>
    <span class="badge"></span>
    <span class="badge"></span>
    <span class="badge wide"></span>
  </section>

  <section class="packages">
    <h2>Hosting Packages</h2>
    <div class="tiers">
      <article class="tier featured">
        <div class="tier-name">e-200</div>
        <ul class="features">
          <li><svg width="10" height="8" viewBox="0 0 10 8"><path d="M1 4 L4 7 L9 1" fill="none" stroke="currentColor" stroke-width="1.6"/></svg>100 MB storage</li>
          <li><svg width="10" height="8" viewBox="0 0 10 8"><path d="M1 4 L4 7 L9 1" fill="none" stroke="currentColor" stroke-width="1.6"/></svg>10 web sites</li>
          <li><svg width="10" height="8" viewBox="0 0 10 8"><path d="M1 4 L4 7 L9 1" fill="none" stroke="currentColor" stroke-width="1.6"/></svg>All-in-one tools</li>
          <li><svg width="10" height="8" viewBox="0 0 10 8"><path d="M1 4 L4 7 L9 1" fill="none" stroke="currentColor" stroke-width="1.6"/></svg>24/7 assistance</li>
        </ul>
        <div class="price"><span class="amount">$149<small>/mo</small></span><span class="order">Order Now</span></div>
      </article>
      <article class="tier">
        <div class="tier-name">e-500</div>
        <ul class="features">
          <li><svg width="10" height="8" viewBox="0 0 10 8"><path d="M1 4 L4 7 L9 1" fill="none" stroke="currentColor" stroke-width="1.6"/></svg>500 MB storage</li>
          <li><svg width="10" height="8" viewBox="0 0 10 8"><path d="M1 4 L4 7 L9 1" fill="none" stroke="currentColor" stroke-width="1.6"/></svg>25 web sites</li>
          <li><svg width="10" height="8" viewBox="0 0 10 8"><path d="M1 4 L4 7 L9 1" fill="none" stroke="currentColor" stroke-width="1.6"/></svg>All-in-one tools</li>
          <li><svg width="10" height="8" viewBox="0 0 10 8"><path d="M1 4 L4 7 L9 1" fill="none" stroke="currentColor" stroke-width="1.6"/></svg>24/7 assistance</li>
        </ul>
        <div class="price"><span class="amount">$249<small>/mo</small></span><span class="order">Order Now</span></div>
      </article>
      <article class="tier">
        <div class="tier-name">e-1000</div>
        <ul class="features">
          <li><svg width="10" height="8" viewBox="0 0 10 8"><path d="M1 4 L4 7 L9 1" fill="none" stroke="currentColor" stroke-width="1.6"/></svg>1 GB storage</li>
          <li><svg width="10" height="8" viewBox="0 0 10 8"><path d="M1 4 L4 7 L9 1" fill="none" stroke="currentColor" stroke-width="1.6"/></svg>50 web sites</li>
          <li><svg width="10" height="8" viewBox="0 0 10 8"><path d="M1 4 L4 7 L9 1" fill="none" stroke="currentColor" stroke-width="1.6"/></svg>All-in-one tools</li>
          <li><svg width="10" height="8" viewBox="0 0 10 8"><path d="M1 4 L4 7 L9 1" fill="none" stroke="currentColor" stroke-width="1.6"/></svg>24/7 assistance</li>
        </ul>
        <div class="price"><span class="amount">$549<small>/mo</small></span><span class="order">Order Now</span></div>
      </article>
    </div>
  </section>
</body>
</html>
```